Android Payment Application UI Design

We require a UI/UX design for an existing Android card-based payment application.

We're looking to improve the look + feel of the existing app. What we're after:
- Colour palette options
- Fonts
- Icons

See attached document for existing screen types, icons, etc.

All resources provided must be royalty free.

It's to run on a specialised device, with 720 x 1280 pixel resolution, in portrait only (landscape not required).

Please provide mockup examples of the new screen layout applied to the existing screens in the document.

Target Market(s)

Retail business users

Font styles to use
Sans Serif

Colors

Designer to choose colors to be used in the design.

Requirements
Must have
• Looking for
• - modern design
• - simple colours, easy-to-read sans-serif fonts
• - cohesive, consistent design between screens

```html
<!DOCTYPE html>
<html lang="en">
<head>
<meta charset="utf-8">
<title>OrvoPay – Screen Set</title>
<link href="https://fonts.googleapis.com/css2?family=Lato:wght@300;400;700;900&display=swap" rel="stylesheet">
<style>
:root{
  --bg:#e9ecf1;
  --indigo:#2b2cb3;
  --blue:#1f4fd9;
  --sky:#1f78e6;
  --ink:#1d1f3a;
  --muted:#9aa0b4;
  --line:#e4e7ef;
  --white:#ffffff;
  --paper:#f7f8fb;
}
*{box-sizing:border-box;margin:0;padding:0}
html,body{width:1200px;height:750px;overflow:hidden}
body{background:var(--bg);font-family:"Lato",sans-serif;color:var(--ink)}
.board{position:relative;width:1200px;height:750px;display:flex;gap:22px;justify-content:center;align-items:center}
.screen{position:relative;width:210px;height:373px;border-radius:6px;overflow:hidden;background:var(--white);box-shadow:0 12px 30px rgba(40,50,90,.12);display:flex;flex-direction:column}
.status{height:16px;display:flex;justify-content:space-between;align-items:center;padding:0 8px;font-size:6px;color:var(--white)}
.status--dark{color:var(--white)}
.appbar{display:flex;align-items:center;justify-content:space-between;padding:4px 10px;color:var(--white)}
.brand{font-weight:900;font-size:11px;letter-spacing:.5px;display:flex;align-items:center;gap:4px}
.brand-dot{width:7px;height:7px;border-radius:50%;background:#6fc3ff}
.avatar{width:14px;height:14px;border-radius:50%;background:#c9cde0;border:2px solid var(--white)}
.back{width:10px;height:10px}
/* amount */
.header{background:var(--indigo);color:var(--white)}
.header-body{padding:10px 16px 14px}
.title{font-weight:700;font-size:17px}
.subtitle{font-size:7px;opacity:.8;margin-top:2px}
.label{font-size:5.5px;letter-spacing:1px;text-transform:uppercase;opacity:.6;margin-top:12px}
.amount{font-weight:300;font-size:24px;color:#7ea6ff}
.proceed{background:var(--sky);color:var(--white);font-size:7px;font-weight:700;letter-spacing:1px;text-align:center;padding:12px 0}
.keypad{flex:1;display:grid;grid-template-columns:repeat(3,1fr);align-items:center;justify-items:center;padding:10px 18px 16px;color:var(--muted);font-size:11px}
/* full colour screens */
.screen--blue{background:var(--blue);color:var(--white)}
.screen--indigo{background:var(--indigo);color:var(--white)}
.center{flex:1;display:flex;flex-direction:column;align-items:center;text-align:center;padding:0 20px}
.big-title{font-weight:700;font-size:17px;line-height:1.15;margin-top:56px}
.note{font-size:7px;opacity:.85;margin-top:6px;line-height:1.4}
.tick{margin:26px 0 24px}
.logo-name{font-weight:900;font-size:16px;margin-top:10px}
.logo-circle{width:44px;height:44px;border-radius:50%;background:#4aa8ff;margin-top:92px}
.pill{background:var(--white);color:var(--indigo);border-radius:20px;width:150px;padding:9px 0;font-size:8px;font-weight:700;margin-top:50px}
.link{font-size:8px;font-weight:700;margin-top:10px}
.version{font-size:6px;opacity:.7;margin-top:auto;margin-bottom:16px}
/* home */
.home{background:var(--paper)}
.greeting{padding:12px 14px 0}
.greeting h1{font-size:15px;font-weight:900;line-height:1.1}
.greeting p{font-size:6.5px;color:var(--muted);margin-top:3px}
.tiles{display:flex;gap:8px;padding:12px 14px 0}
.tile{flex:1;background:var(--white);border-radius:4px;padding:10px 8px;box-shadow:0 4px 10px rgba(40,50,90,.06)}
.tile-name{font-size:8px;font-weight:700;color:var(--indigo);margin-top:6px}
.tile-desc{font-size:5.5px;color:var(--muted);margin-top:2px}
.section{padding:14px 14px 0}
.section h2{font-size:10px;font-weight:900;color:var(--indigo)}
.section p{font-size:6px;color:var(--muted);margin-top:2px}
.chips{display:flex;gap:4px;margin-top:8px}
.chip{background:var(--sky);color:var(--white);border-radius:10px;font-size:6px;font-weight:700;padding:4px 7px;white-space:nowrap}
.activity{margin-top:8px;font-size:5.5px;display:flex;gap:8px}
.activity b{font-weight:900;letter-spacing:.5px}
.activity span{color:var(--muted)}
/* pin */
.pin-body{flex:1;padding:16px 16px 0;display:flex;flex-direction:column}
.pin-body .title{color:var(--ink)}
.pin-body .subtitle{color:var(--muted);opacity:1}
.pin-field{margin-top:40px;text-align:center;font-size:5.5px;letter-spacing:1px;color:var(--muted)}
.dots{display:flex;gap:6px;justify-content:center;margin-top:8px}
.dots i{width:3px;height:3px;border-radius:50%;background:var(--muted)}
.pin-link{text-align:center;font-size:6px;font-weight:700;letter-spacing:1px;color:var(--sky);margin-top:18px}
.pin-foot{background:var(--sky);color:var(--white);display:flex;justify-content:space-between;align-items:center;padding:12px 16px}
.pin-foot .amount{color:var(--white);font-size:16px}
.pin-foot span{font-size:7px;font-weight:700;letter-spacing:1px}
</style>
</head>
<body>
<main class="board">

  <section class="screen amount-entry">
    <div class="header">
      <div class="status"><span>▮▮▮</span><span>9:41 AM</span><span>100%</span></div>
      <div class="appbar">
        <svg class="back" viewBox="0 0 10 10"><path d="M9 5H1M4 2L1 5l3 3" stroke="#fff" stroke-width="1.2" fill="none"/></svg>
        <div class="brand"><span class="brand-dot"></span>Orvo</div>
        <div class="avatar"></div>
      </div>
      <div class="header-body">
        <div class="title">Amount Entry</div>
        <div class="subtitle">Check your sale</div>
        <div class="label">Enter amount</div>
        <div class="amount">09.56</div>
      </div>
    </div>
    <div class="proceed">PROCEED</div>
    <div class="keypad">
      <span>1</span><span>2</span><span>3</span>
      <span>4</span><span>5</span><span>6</span>
      <span>7</span><span>8</span><span>9</span>
      <span>•</span><span>0</span>
      <svg width="11" height="8" viewBox="0 0 11 8"><path d="M3 0h8v8H3L0 4z" fill="#c3c8d6"/><path d="M5 2l3 4M8 2L5 6" stroke="#fff" stroke-width="1"/></svg>
    </div>
  </section>

  <section class="screen screen--blue testing-connection">
    <div class="status"><span>▮▮▮</span><span>9:41 AM</span><span>100%</span></div>
    <div class="center">
      <div class="big-title">Testing<br>Connection</div>
      <div class="note">Please wait a sec.</div>
      <svg class="tick" width="64" height="64" viewBox="0 0 64 64"><circle cx="32" cy="32" r="30" stroke="#fff" stroke-width="2" fill="none"/><path d="M20 34l8 7 16-18" stroke="#fff" stroke-width="2" fill="none"/></svg>
      <div class="note">Congratulations, you are authorized. Double Tap anywhere to get back to home screen</div>
    </div>
  </section>

  <section class="screen screen--indigo splash">
    <div class="status"><span>▮▮▮</span><span>9:41 AM</span><span>100%</span></div>
    <div class="center">
      <div class="logo-circle"></div>
      <div class="logo-name">OrvoPay</div>
      <div class="note">your payment partner choice</div>
      <div class="pill">Log In</div>
      <div class="link">Sign Up</div>
      <div class="version">Ver 0.0.1</div>
    </div>
  </section>

  <section class="screen home">
    <div class="header">
      <div class="status"><span>▮▮▮</span><span>9:41 AM</span><span>100%</span></div>
      <div class="appbar">
        <svg class="back" viewBox="0 0 10 10"><path d="M9 5H1M4 2L1 5l3 3" stroke="#fff" stroke-width="1.2" fill="none"/></svg>
        <div class="brand"><span class="brand-dot"></span>Orvo</div>
        <div class="avatar"></div>
      </div>
    </div>
    <div class="greeting">
      <h1>Hello there,<br>John!</h1>
      <p>How can we help you?</p>
    </div>
    <div class="tiles">
      <div class="tile">
        <svg width="14" height="10" viewBox="0 0 14 10"><rect x=".5" y=".5" width="13" height="9" rx="1" stroke="#1f78e6" fill="none"/><path d="M.5 3.5h13" stroke="#1f78e6"/></svg>
        <div class="tile-name">Sale</div>
        <div class="tile-desc">Check your sales</div>
      </div>
      <div class="tile">
        <svg width="12" height="12" viewBox="0 0 12 12"><path d="M10 5a4 4 0 0 0-7.5-1.5M2 7a4 4 0 0 0 7.5 1.5M2.5 1v2.5H5M9.5 11V8.5H7" stroke="#1f78e6" fill="none"/></svg>
        <div class="tile-name">Reversal</div>
        <div class="tile-desc">Put small description</div>
      </div>
    </div>
    <div class="section">
      <h2>Admin</h2>
      <p>Short description about admin menu</p>
      <div class="chips"><span class="chip">Payment</span><span class="chip">Connect An Account</span><span class="chip">Manage</span></div>
    </div>
    <div class="section">
      <h2>Recent Activity</h2>
      <p>Small description for Activity</p>
      <div class="activity"><b>YESTERDAY</b><span>Your terminal was connected to your account</span></div>
    </div>
  </section>

  <section class="screen enter-pin">
    <div class="header">
      <div class="status"><span>▮▮▮</span><span>9:41 AM</span><span>100%</span></div>
      <div class="appbar">
        <svg class="back" viewBox="0 0 10 10"><path d="M9 5H1M4 2L1 5l3 3" stroke="#fff" stroke-width="1.2" fill="none"/></svg>
        <div class="brand"><span class="brand-dot"></span>Orvo</div>
        <div class="avatar"></div>
      </div>
    </div>
    <div class="pin-body">
      <div class="title">Enter Pin</div>
      <div class="subtitle">Please enter your PIN</div>
      <div class="pin-field">4 DIGIT PIN</div>
      <div class="dots"><i></i><i></i><i></i><i></i></div>
      <div class="pin-link">ENTER YOUR PIN</div>
    </div>
    <div class="pin-foot"><div class="amount">09.56</div><span>PROCEED</span></div>
  </section>

</main>
</body>
</html>
```